Business cards and letterhead
cards and letterhead
Thanks all designers for your hard work.
Does anybody have anything different than just the swirl line through it?
I realy want the web address to stand out somehow, everybody just keep putting it in small letters...
Let's just leave off the email and make the web address stand out better.
creater I like #18 in black, the RT gets lost on the background. could it have a small white outline or something so it stands out. Website address must be on there, my email is not that important. Thanks
I like the color on there it makes it pop.
I want the web address to stand out. Thanks

```html
<!DOCTYPE html>
<html lang="en">
<head>
<meta charset="utf-8">
<title>RT Auto Sales – Stationery</title>
<link rel="stylesheet" href="https://fonts.googleapis.com/css2?family=Arimo:ital,wght@0,400;0,700;1,700&display=swap">
<style>
  :root {
    --navy: #1f2f7a;
    --red: #b3161c;
    --red-dark: #7d0d10;
    --ink: #333a45;
    --paper: #ffffff;
    --backdrop: #e8e3da;
    --rule: #b9bcc4;
  }
  * { margin: 0; padding: 0; box-sizing: border-box; }
  html, body { width: 1200px; height: 935px; overflow: hidden; }
  body {
    background: var(--backdrop);
    font-family: "Arimo", Arial, sans-serif;
    color: var(--ink);
    position: relative;
  }
  .sheet {
    position: absolute;
    background: var(--paper);
    box-shadow: 0 4px 14px rgba(0,0,0,.22);
    overflow: hidden;
  }
  .swoosh { position: absolute; left: 0; bottom: 0; width: 100%; }
  .web {
    position: absolute; right: 22px; color: #fff; font-weight: 700;
    letter-spacing: .3px;
  }
  .brand {
    display: flex; align-items: center; gap: 8px;
    color: var(--navy); font-weight: 700; text-transform: uppercase;
    line-height: 1;
  }
  .brand-mark { background: var(--navy); flex: none; }

  /* Fax sheet */
  .fax { left: 45px; top: 164px; width: 520px; height: 746px; }
  .fax .brand { position: absolute; left: 36px; top: 40px; font-size: 34px; }
  .fax .brand-mark { width: 26px; height: 26px; }
  .fax-title { position: absolute; left: 36px; top: 172px; font-size: 34px; font-weight: 700; color: #222; }
  .fax-form { position: absolute; left: 36px; top: 250px; width: 200px; list-style: none; }
  .fax-form li {
    display: flex; align-items: flex-end; gap: 6px;
    font-size: 11px; font-weight: 700; font-style: italic; height: 34px;
  }
  .fax-form li span { flex: 1; border-bottom: 1px solid var(--rule); height: 1px; }
  .fax-checks { position: absolute; left: 36px; top: 414px; display: flex; gap: 28px; font-size: 11px; }
  .fax-checks label { display: flex; align-items: center; gap: 6px; }
  .fax-checks i { width: 11px; height: 11px; border: 1px solid #888; display: inline-block; }

  /* Letterhead */
  .letterhead { left: 202px; top: 25px; width: 531px; height: 847px; }
  .letterhead .brand { position: absolute; left: 40px; top: 50px; font-size: 34px; }
  .letterhead .brand-mark { width: 26px; height: 26px; }
  .letter-contact { position: absolute; left: 420px; top: 36px; font-size: 9px; line-height: 1.5; font-style: normal; }
  .letter-contact b { color: var(--red); }
  .letterhead .web { bottom: 24px; font-size: 20px; }

  /* Envelope */
  .envelope { left: 525px; top: 215px; width: 612px; height: 278px; }
  .env-flap { position: absolute; left: 0; top: 0; width: 100%; height: 34px; }
  .envelope .brand { position: absolute; left: 26px; top: 82px; font-size: 30px; }
  .envelope .brand-mark { width: 22px; height: 22px; }
  .env-address { position: absolute; left: 26px; top: 168px; font-size: 15px; line-height: 1.4; color: #222; font-style: normal; }
  .envelope .web { bottom: 14px; font-size: 18px; }

  /* Business cards */
  .card { border-radius: 10px; }
  .card-front { left: 854px; top: 568px; width: 252px; height: 127px; }
  .card-front .brand { position: absolute; left: 16px; top: 46px; font-size: 18px; }
  .card-front .brand-mark { width: 14px; height: 14px; }
  .card-band { position: absolute; right: 0; top: 0; width: 140px; height: 36px; }
  .card-name { position: absolute; right: 12px; top: 6px; text-align: right; color: #fff; font-size: 10px; font-weight: 700; line-height: 1.3; }
  .card-name small { font-weight: 400; font-size: 8px; display: block; }
  .card-details { position: absolute; left: 16px; right: 12px; bottom: 14px; display: flex; justify-content: space-between; font-size: 7px; line-height: 1.45; }
  .card-details strong { color: var(--navy); }
  .card-back { left: 854px; top: 720px; width: 237px; height: 126px; }
  .card-back .brand { position: absolute; left: 18px; top: 28px; font-size: 18px; }
  .card-back .brand-mark { width: 14px; height: 14px; }
  .card-back .web { bottom: 8px; right: 14px; font-size: 13px; }
</style>
</head>
<body>

<section class="sheet fax" aria-label="Fax cover sheet">
  <div class="brand"><span class="brand-mark"></span>RT Auto Sales</div>
  <h1 class="fax-title">FAX</h1>
  <ul class="fax-form">
    <li>To :<span></span></li>
    <li>Fax :<span></span></li>
    <li>Phone :<span></span></li>
    <li>Re :<span></span></li>
  </ul>
  <div class="fax-checks">
    <label><i></i>Urgent</label>
    <label><i></i>For Review</label>
  </div>
  <svg class="swoosh" viewBox="0 0 100 30" preserveAspectRatio="none" height="150" aria-hidden="true">
    <path d="M0 8 C40 30 70 20 100 1 L100 30 L0 30Z" fill="var(--navy)"/>
    <path d="M0 12 C40 33 70 23 100 5 L100 30 L0 30Z" fill="#fff"/>
    <path d="M0 14 C40 35 70 25 100 7 L100 30 L0 30Z" fill="var(--red)"/>
  </svg>
</section>

<section class="sheet letterhead" aria-label="Letterhead">
  <div class="brand"><span class="brand-mark"></span>RT Auto Sales</div>
  <address class="letter-contact">
    418 Cedar Ridge Rd.<br>Lakeview, TX 75000<br><br>
    <b>P.</b> 555-014-2270<br>
    <b>F.</b> 555-014-2281<br>
    <b>E.</b> dkerr@rtautosales.biz
  </address>
  <svg class="swoosh" viewBox="0 0 100 30" preserveAspectRatio="none" height="170" aria-hidden="true">
    <defs>
      <linearGradient id="redFade" x1="0" y1="0" x2="1" y2="0">
        <stop offset="0" stop-color="var(--red-dark)"/>
        <stop offset="1" stop-color="var(--red)"/>
      </linearGradient>
    </defs>
    <path d="M0 6 C40 30 70 20 100 0 L100 30 L0 30Z" fill="var(--navy)"/>
    <path d="M0 10 C40 33 70 23 100 4 L100 30 L0 30Z" fill="#fff"/>
    <path d="M0 13 C40 35 70 25 100 6 L100 30 L0 30Z" fill="url(#redFade)"/>
  </svg>
  <span class="web">www.rtautosales.biz</span>
</section>

<section class="sheet envelope" aria-label="Envelope">
  <svg class="env-flap" viewBox="0 0 100 10" preserveAspectRatio="none" aria-hidden="true">
    <path d="M0 0 H100 V5 C70 10 30 10 0 8Z" fill="var(--red)"/>
  </svg>
  <div class="brand"><span class="brand-mark"></span>RT Auto Sales</div>
  <address class="env-address">418 Cedar Ridge Rd.<br>Lakeview, TX 75000</address>
  <svg class="swoosh" viewBox="0 0 100 30" preserveAspectRatio="none" height="110" aria-hidden="true">
    <path d="M0 26 C40 24 70 14 100 2 L100 30 L0 30Z" fill="var(--navy)"/>
    <path d="M0 28 C40 26 70 17 100 7 L100 30 L0 30Z" fill="#fff"/>
    <path d="M0 29 C40 28 70 19 100 10 L100 30 L0 30Z" fill="var(--red)"/>
  </svg>
  <span class="web">www.rtautosales.biz</span>
</section>

<section class="sheet card card-front" aria-label="Business card front">
  <svg class="card-band" viewBox="0 0 100 30" preserveAspectRatio="none" aria-hidden="true">
    <path d="M10 0 H100 V30 H0 C8 22 8 8 10 0Z" fill="var(--red)"/>
  </svg>
  <div class="card-name">Daniel Kerr<small>Owner</small></div>
  <div class="brand"><span class="brand-mark"></span>RT Auto Sales</div>
  <div class="card-details">
    <span>418 Cedar Ridge Rd.<br>Lakeview, TX 75000</span>
    <span>P. 555-014-2270<br>F. 555-014-2281<br><strong>www.rtautosales.biz</strong></span>
  </div>
</section>

<section class="sheet card card-back" aria-label="Business card back">
  <div class="brand"><span class="brand-mark"></span>RT Auto Sales</div>
  <svg class="swoosh" viewBox="0 0 100 30" preserveAspectRatio="none" height="60" aria-hidden="true">
    <path d="M0 6 C40 11 70 5 100 0 L100 30 L0 30Z" fill="var(--navy)"/>
    <path d="M0 8 C40 13 70 7 100 2 L100 30 L0 30Z" fill="#fff"/>
    <path d="M0 10 C40 15 70 9 100 4 L100 30 L0 30Z" fill="var(--red)"/>
  </svg>
  <span class="web">www.rtautosales.biz</span>
</section>

</body>
</html>
```